Maple Grin
Pediatric and Family Dentistry
Maple Grin -
Creative Brief
Bright & Fun-filled
Doria Velcott, DMD
Pediatric Dentist
1746 Brannock Lane, Suite 410 Fairfax, VA 22157
maplegrinoffice@brindlemail.com
MapleGrinClinic.com
We would like a second name on this card as listed below Name: Lorna Tevick, DDS Title: General Dentist
Appointment For: Date: Time:

```html
<!DOCTYPE html>
<html lang="en">
<head>
<meta charset="utf-8">
<title>Maple Grin – Stationery</title>
<link href="https://fonts.googleapis.com/css2?family=Nunito:wght@400;700;800&display=swap" rel="stylesheet">
<style>
  :root {
    --paper: #ffffff;
    --board: #ffffff;
    --frame: #e2e2e2;
    --sun: #f6c01b;
    --orange: #f08a1f;
    --ink: #4a4a4a;
    --muted: #8a8a8a;
    --faint: #fbe3bd;
    --shadow: rgba(0,0,0,0.22);
  }
  * { box-sizing: border-box; margin: 0; padding: 0; }
  html, body { width: 1200px; height: 681px; overflow: hidden; background: var(--board); }
  body { font-family: "Nunito", Arial, sans-serif; color: var(--ink); position: relative; }

  .board-frame { position: absolute; left: 22px; top: 24px; width: 1156px; height: 633px; border: 1px solid var(--frame); border-top: none; border-right: none; }

  .sheet { position: absolute; background: var(--paper); box-shadow: 2px 3px 8px var(--shadow); overflow: hidden; }

  .wordmark { display: flex; align-items: center; gap: 6px; }
  .wordmark .dot { border-radius: 50%; background: var(--sun); flex: none; }
  .wordmark .name { font-weight: 800; color: var(--orange); white-space: nowrap; line-height: 1; }
  .tagline { color: var(--muted); white-space: nowrap; }

  .rule { position: absolute; height: 4px; }
  .rule.sun { background: var(--sun); }
  .rule.orange { background: var(--orange); }

  .ring { position: absolute; border-radius: 50%; border: solid var(--faint); }

  /* envelope front */
  .envelope-front { left: 67px; top: 91px; width: 475px; height: 216px; }
  .envelope-front .brand { position: absolute; left: 18px; top: 20px; }
  .envelope-front .wordmark .dot { width: 20px; height: 20px; }
  .envelope-front .wordmark .name { font-size: 26px; }
  .envelope-front .tagline { font-size: 9px; margin-left: 26px; margin-top: 2px; }
  .envelope-front .return { position: absolute; left: 18px; top: 88px; font-size: 8px; color: var(--ink); }

  /* envelope back */
  .envelope-back { left: 67px; top: 360px; width: 475px; height: 252px; }
  .envelope-back svg.flap { position: absolute; inset: 0; }
  .envelope-back .seal { position: absolute; left: 50%; top: 104px; transform: translateX(-50%); }
  .envelope-back .wordmark .dot { width: 12px; height: 12px; }
  .envelope-back .wordmark .name { font-size: 15px; }

  /* letterhead */
  .letterhead { left: 612px; top: 48px; width: 343px; height: 581px; }
  .letterhead .brand { position: absolute; left: 16px; top: 38px; }
  .letterhead .wordmark .dot { width: 18px; height: 18px; }
  .letterhead .wordmark .name { font-size: 22px; }
  .letterhead .tagline { font-size: 8px; margin-left: 24px; margin-top: 2px; }
  .letterhead .footer { position: absolute; left: 16px; bottom: 20px; font-size: 6.5px; line-height: 1.5; color: var(--ink); }

  /* business cards */
  .card { width: 161px; height: 112px; }
  .card-front { left: 967px; top: 180px; }
  .card-front .brand { position: absolute; left: 8px; top: 14px; }
  .card-front .wordmark { gap: 3px; }
  .card-front .wordmark .dot { width: 9px; height: 9px; }
  .card-front .wordmark .name { font-size: 12px; }
  .card-front .tagline { font-size: 4.5px; margin-left: 12px; margin-top: 1px; }
  .card-front .people { position: absolute; left: 8px; top: 48px; font-size: 5px; line-height: 1.35; }
  .card-front .people .person { margin-bottom: 3px; }
  .card-front .people b { color: var(--orange); font-weight: 700; }
  .card-front .contact { position: absolute; right: 8px; top: 12px; font-size: 4.2px; line-height: 1.45; text-align: right; color: var(--ink); }

  .card-back { left: 967px; top: 305px; }
  .card-back .seal { position: absolute; left: 12px; top: 14px; }
  .card-back .seal .dot { width: 14px; height: 14px; }
  .card-back .appointment { position: absolute; left: 44px; top: 36px; font-size: 5px; color: var(--ink); }
  .card-back .appointment .title { color: var(--orange); font-weight: 700; margin-bottom: 6px; }
  .card-back .field { display: flex; align-items: flex-end; gap: 3px; margin-bottom: 6px; }
  .card-back .field span.line { display: block; width: 60px; border-bottom: 0.6px solid var(--muted); }
</style>
</head>
<body>
  <div class="board-frame"></div>

  <!-- envelope front -->
  <section class="sheet envelope-front">
    <div class="brand">
      <div class="wordmark"><span class="dot"></span><span class="name">Maple Grin</span></div>
      <div class="tagline">Pediatric and Family Dentistry</div>
    </div>
    <div class="rule sun" style="left:205px; top:42px; width:70px;"></div>
    <div class="rule orange" style="left:283px; top:42px; width:192px;"></div>
    <p class="return">1746 Brannock Lane, Suite 410 | Fairfax, VA 22157</p>
    <div class="ring" style="right:-40px; top:95px; width:110px; height:110px; border-width:9px;"></div>
  </section>

  <!-- envelope back -->
  <section class="sheet envelope-back">
    <svg class="flap" width="475" height="252" viewBox="0 0 475 252" aria-hidden="true">
      <path d="M2 2 Q 10 40 40 52 L 200 100 Q 237 112 274 100 L 435 52 Q 465 40 473 2" fill="none" stroke="#9a9a9a" stroke-width="1.2"/>
    </svg>
    <div class="seal">
      <div class="wordmark"><span class="dot"></span><span class="name">Maple Grin</span></div>
    </div>
  </section>

  <!-- letterhead -->
  <section class="sheet letterhead">
    <div class="brand">
      <div class="wordmark"><span class="dot"></span><span class="name">Maple Grin</span></div>
      <div class="tagline">Pediatric and Family Dentistry</div>
    </div>
    <div class="rule sun" style="left:190px; top:50px; width:50px; height:3px;"></div>
    <div class="rule orange" style="left:246px; top:50px; width:97px; height:3px;"></div>
    <div class="ring" style="right:-60px; top:330px; width:190px; height:190px; border-width:14px;"></div>
    <div class="footer">
      1746 Brannock Lane, Suite 410 | Fairfax, VA 22157<br>
      Phone: (703) 555-0182 | Fax: (703) 555-0190<br>
      maplegrinoffice@brindlemail.com | MapleGrinClinic.com
    </div>
  </section>

  <!-- business card front -->
  <section class="sheet card card-front">
    <div class="brand">
      <div class="wordmark"><span class="dot"></span><span class="name">Maple Grin</span></div>
      <div class="tagline">Pediatric and Family Dentistry</div>
    </div>
    <div class="contact">
      1746 Brannock Lane,<br>Suite 410<br>Fairfax, VA 22157<br>
      (703) 555-0182<br>maplegrinoffice@<br>brindlemail.com<br>MapleGrinClinic.com
    </div>
    <div class="people">
      <div class="person"><b>Doria Velcott, DMD</b><br>Pediatric Dentist</div>
      <div class="person"><b>Lorna Tevick, DDS</b><br>General Dentist</div>
    </div>
    <div class="ring" style="right:-22px; bottom:-26px; width:74px; height:74px; border-width:7px;"></div>
  </section>

  <!-- business card back -->
  <section class="sheet card card-back">
    <div class="seal wordmark"><span class="dot"></span></div>
    <div class="appointment">
      <div class="title">Appointment For:</div>
      <div class="field">Date: <span class="line"></span></div>
      <div class="field">Time: <span class="line"></span></div>
    </div>
    <div class="ring" style="right:-24px; bottom:-24px; width:70px; height:70px; border-width:6px;"></div>
  </section>
</body>
</html>
```